Boutique Film/TV Company needs Business Card Design

Please see our website for background on our company and look of our current logo: www.lumarocpictures.ca

Pantone 314U is our main colour.

Target Market(s)

Network of peers, funders and broadcasters.

Industry/Entity Type

Business

Requirements
Must have
• We would like rounded corners and the height of the card to be shorter than traditional (maybe?!)

It's important that we have room for our office address, office number, cell number, email address, website, facebook and linked-in info (though not all of us have a linked-in account).

Would like the logo to keep the exclamation marks over the letters but the tag line/tag words of "film - television - interactive" can stay or go or... surprise me!

Nice to have
• Silky matte finish.

We are open to a change in the font of our logo/name.

```html
<!DOCTYPE html>
<html lang="en">
<head>
<meta charset="utf-8">
<title>Lumaroc Pictures – Business Card</title>
<link rel="stylesheet" href="https://fonts.googleapis.com/css2?family=Ubuntu:wght@400;500;700&display=swap">
<style>
  :root {
    --brand-teal: #1a87a5;
    --brand-teal-deep: #137391;
    --paper: #ffffff;
    --ink: #2b2f33;
    --backdrop: #dfe5e8;
  }
  * { box-sizing: border-box; margin: 0; padding: 0; }
  html, body {
    width: 1200px; height: 960px; overflow: hidden;
    background: var(--backdrop);
    font-family: "Ubuntu", sans-serif;
  }
  .sheet {
    width: 1200px; height: 960px;
    display: flex; flex-direction: column;
    align-items: center; justify-content: center; gap: 60px;
  }
  .card {
    position: relative;
    width: 620px; height: 330px;
    border-radius: 44px;
    overflow: hidden;
    box-shadow: 0 10px 30px rgba(20, 40, 50, 0.18);
  }

  /* Front side */
  .card--front { background: var(--paper); }
  .name-band {
    position: absolute; left: 0; top: 78px;
    width: 560px; height: 100px;
    background: var(--brand-teal);
    color: var(--paper);
    padding: 22px 0 0 62px;
  }
  .name-band__name { font-size: 31px; font-weight: 400; letter-spacing: 0.2px; }
  .name-band__title { font-size: 19px; font-weight: 400; margin-top: 6px; }
  .contact-list {
    position: absolute; left: 62px; top: 206px;
    list-style: none;
    font-size: 15.5px; color: var(--ink); line-height: 19px;
  }
  .contact-list li { display: flex; align-items: center; gap: 14px; }
  .contact-list svg { width: 13px; height: 13px; flex: none; fill: var(--brand-teal); }
  .contact-list .company { font-weight: 700; }

  /* Back side */
  .card--back {
    background: linear-gradient(135deg, var(--brand-teal) 0%, var(--brand-teal-deep) 100%);
    color: var(--paper);
  }
  .wordmark {
    position: absolute; left: 0; right: 0; top: 70px;
    text-align: center;
    font-size: 86px; font-weight: 400; letter-spacing: 1px;
  }
  .tagline {
    position: absolute; left: 0; right: 0; top: 178px;
    text-align: center;
    font-size: 17px; font-weight: 700; letter-spacing: 0.4px;
  }
  .web-strip {
    position: absolute; left: 0; right: 0; bottom: 34px;
    height: 34px; background: var(--paper);
    color: var(--brand-teal);
    display: flex; align-items: center; justify-content: center;
    font-size: 16px; font-weight: 500; letter-spacing: 5px;
  }
</style>
</head>
<body>
<main class="sheet">

  <section class="card card--front" aria-label="Card front">
    <div class="name-band">
      <p class="name-band__name">Nadia Kerrigan</p>
      <p class="name-band__title">Manager</p>
    </div>
    <ul class="contact-list">
      <li>
        <svg viewBox="0 0 16 16" aria-hidden="true"><path d="M3 1l3 3-1.5 2a9 9 0 0 0 5.5 5.5L12 10l3 3-2 2C7 15 1 9 1 3z"/></svg>
        416.555.0142
      </li>
      <li>
        <svg viewBox="0 0 16 16" aria-hidden="true"><path d="M4 0h8v16H4z M5.5 2v8h5V2z"/></svg>
        416.555.0178
      </li>
      <li>
        <svg viewBox="0 0 16 16" aria-hidden="true"><path d="M0 3h16v10H0z M1.5 4.5L8 9l6.5-4.5v-0.2H1.5z" fill-rule="evenodd"/></svg>
        nadia@lumarocpictures.ca
      </li>
      <li>
        <svg viewBox="0 0 16 16" aria-hidden="true"><rect x="1" y="1" width="14" height="14" rx="2"/></svg>
        /lumarocpictures.com
      </li>
      <li>
        <svg viewBox="0 0 16 16" aria-hidden="true"><rect x="1" y="1" width="14" height="14" rx="2"/></svg>
        /nadia-kerrigan
      </li>
      <li>
        <svg viewBox="0 0 16 16" aria-hidden="true"><path d="M8 0a5.5 5.5 0 0 1 5.5 5.5C13.5 10 8 16 8 16S2.5 10 2.5 5.5A5.5 5.5 0 0 1 8 0z M8 3.5a2 2 0 1 0 0 4 2 2 0 0 0 0-4z" fill-rule="evenodd"/></svg>
        <span><span class="company">Lumaroc Pictures Inc.</span> 42 Alder Crescent, Toronto, ON, M4E 2K9</span>
      </li>
    </ul>
  </section>

  <section class="card card--back" aria-label="Card back">
    <p class="wordmark">Lumaroc</p>
    <p class="tagline">Films • Television • Interactive</p>
    <p class="web-strip">www.lumarocpictures.ca</p>
  </section>

</main>
</body>
</html>
```